Full redesign of dairy products including Yogurts and milk products

We have been selling milk and yogurts over the past 15 years, we are now expanding into a wider range of dairy products to include flavoured milk and a variety of soft cheeses such as cottage cheese etc. It is now the perfect time to redesign our existing product range to give a fresh and new look to our products. Have a look at our website https://rtvale.co.uk/ for further details. We are rebranding as NUVELKA, I have attached a identify pack to give you a feel of the the design, this is a fresh and bright design that will reflect the fresh and tasteful products we produce. The current milk label cut out is unique to us and I would like to continue using this shape which I have attached, the other labels should be done using regular rectangular rounded edge labels. The following designs are required;
1 x Universal lid (71.5mm) design for all below 120ml Yogurts
-11 x 120 ml Yogurt pot designs
Strawberry
Strawberry Banana
Peach & Apricot
Cherry
Toffee
Vanilla
Natural
Orange
Forest Fruits
Pineapple
Mango
1 x Universal lid (95.5mm)for below yogurts (can be identical to the 120ml Lid)
-4 x 450ml Yogurt Pots
Strawberry
Natural
Toffee
Mango
-1 x Universal (95.5mm) LID for 150ml Greek Yogurt
-4 x Designs for 150ml Greek yogurt POT
Strawberry
Natural
Vanilla
Mango

3 x Flavoured milk labels 2 sizes 250ml & 1lt
Biscotti
Chocolate
Strawberry

Cottage Cheese Lid & Pot 250g

1 x Quark universal Lid (95.5mm)
4 x Quark 250g pots
Natural
Strawberry
Peach & Apricot
Mango

```html
<!DOCTYPE html>
<html lang="en">
<head>
<meta charset="utf-8">
<title>Nuvelka Yogurt 450ml – Theme 01</title>
<link href="https://fonts.googleapis.com/css2?family=Baloo+2:wght@600;700&family=Roboto:wght@400;700&display=swap" rel="stylesheet">
<style>
  :root{
    --canvas:#eceded;
    --ink:#231f20;
    --white:#ffffff;
    --green:#55c24a;
    --green-dark:#2e7a16;
    --strawberry:#d9161b;
    --strawberry-text:#d71920;
    --toffee:#f48f36;
    --toffee-text:#ee7d2d;
    --natural:#d6b43a;
    --natural-text:#a8871a;
    --mango:#fbb20f;
    --mango-text:#a85a24;
  }
  *{box-sizing:border-box;margin:0;padding:0}
  html,body{width:1200px;height:1200px;overflow:hidden;background:var(--canvas);font-family:"Roboto",Arial,sans-serif;color:var(--ink)}
  .sheet{position:relative;width:1200px;height:1200px}

  .lid{position:absolute;left:484px;top:157px;width:232px;height:271px}
  .lid svg{position:absolute;inset:0}
  .lid-brand{position:absolute;left:0;right:0;top:82px;text-align:center;font-family:"Baloo 2",sans-serif;font-weight:700;font-size:34px;color:var(--white);line-height:1}
  .lid-title{position:absolute;left:0;right:0;top:148px;text-align:center;font-family:"Baloo 2",sans-serif;font-weight:700;font-size:50px;color:var(--white);line-height:1}
  .lid-volume{position:absolute;left:0;right:0;top:231px;text-align:center;font-size:16px;color:var(--white)}

  .dim{position:absolute;font-size:19px;color:var(--ink)}
  .dim-width{left:257px;top:444px}
  .dim-height{left:566px;top:608px;transform:rotate(-90deg)}

  .label{position:absolute;width:516px;height:271px;background:var(--band);border:0.6px solid #9a9a9a;overflow:hidden}
  .label svg.wave{position:absolute;inset:0}
  .label--strawberry{left:45px;top:484px;--band:var(--strawberry);--title:var(--strawberry-text)}
  .label--toffee{left:639px;top:484px;--band:var(--toffee);--title:var(--toffee-text)}
  .label--natural{left:45px;top:772px;--band:var(--natural);--title:var(--natural-text)}
  .label--mango{left:639px;top:772px;--band:var(--mango);--title:var(--mango-text)}

  .info{position:absolute;left:22px;top:49px;width:150px;font-size:7px;line-height:1.25}
  .info b{font-weight:700}
  .nutrition{margin-top:8px;width:108px;border:0.7px solid var(--ink);border-radius:4px;overflow:hidden}
  .nutrition-head{background:var(--ink);color:var(--white);font-weight:700;padding:2px 7px;font-size:7px}
  .nutrition table{width:100%;border-collapse:collapse;margin:4px 0 2px}
  .nutrition td{padding:1px 6px;font-size:7px;line-height:1.2}
  .nutrition td:last-child{text-align:right;padding-right:12px}
  .allergen{margin-top:8px}
  .storage{margin-top:9px}

  .brand{position:absolute;left:160px;width:200px;top:26px;text-align:center;font-family:"Baloo 2",sans-serif;font-weight:700;font-size:34px;color:var(--green);line-height:1}
  .title{position:absolute;left:150px;width:220px;top:78px;text-align:center;font-family:"Baloo 2",sans-serif;font-weight:700;font-size:52px;color:var(--title);line-height:1}
  .flavour-art{position:absolute;left:205px;top:154px;width:108px;height:82px;border-radius:50%}
  .flavour-name{position:absolute;left:160px;width:200px;top:246px;text-align:center;color:var(--white);font-size:11px;letter-spacing:.3px}

  .dates{position:absolute;left:371px;top:108px;font-size:9.5px;line-height:1.1}
  .dates td{padding:0 3px 0 0;white-space:nowrap}
  .maker{position:absolute;left:360px;width:142px;top:161px;text-align:center;font-size:9px;line-height:1.15}
  .maker b{font-weight:700}

  .theme{position:absolute;left:0;right:0;top:1130px;text-align:center;font-size:20px}
</style>
</head>
<body>
<svg width="0" height="0" style="position:absolute">
  <defs>
    <path id="label-wave" d="M0 24 C60 18 100 30 150 28 C200 26 240 6 300 16 C330 22 350 28 370 24 L516 24 L516 236 C480 232 440 240 400 232 C380 228 360 210 340 204 C300 194 270 198 240 208 C200 220 180 228 160 236 C120 246 60 230 0 238 Z"/>
  </defs>
</svg>

<div class="sheet">
  <div class="lid">
    <svg viewBox="0 0 232 271" width="232" height="271">
      <defs><clipPath id="lid-shape"><path d="M104 6 Q116 -4 128 6 L200 72 A117 117 0 1 1 32 72 Z"/></clipPath></defs>
      <g clip-path="url(#lid-shape)">
        <rect width="232" height="271" fill="var(--green)"/>
        <rect y="226" width="232" height="50" fill="var(--green-dark)"/>
      </g>
    </svg>
    <div class="lid-brand">Nuvelka</div>
    <div class="lid-title">Yogurt</div>
    <div class="lid-volume">450ml</div>
  </div>

  <div class="dim dim-width">219</div>
  <div class="dim dim-height">115</div>

  <div class="label label--strawberry">
    <svg class="wave" viewBox="0 0 516 271"><use href="#label-wave" fill="#fff"/></svg>
    <div class="info">
      <b>Ingredients:</b><br>Milk, Strawberries (15%), Sugar,<br>Natural Flavors, Pectin, Live Cultures.
      <div class="nutrition"><div class="nutrition-head">Nutritional Info. (per 100g)</div>
        <table><tr><td>Calories</td><td>120</td></tr><tr><td>Total Fat</td><td>4g</td></tr><tr><td>Saturated Fat</td><td>2.5g</td></tr><tr><td>Carbohydrates</td><td>16g</td></tr><tr><td>Sugars</td><td>14g</td></tr><tr><td>Protein</td><td>5g</td></tr><tr><td>Calcium</td><td>150mg</td></tr></table></div>
      <div class="allergen"><b>Allergen Information:</b> Contains milk.</div>
      <div class="storage"><b>Storage Instructions:</b><br>Keep refrigerated at 4°C or below.<br>Consume within 5 days of opening.</div>
    </div>
    <div class="brand">Nuvelka</div>
    <div class="title">Yogurt</div>
    <div class="flavour-art" role="img" aria-label="Photo of fresh strawberries" style="background:radial-gradient(circle,#d8242a 40%,#4f8f2e 75%,transparent 76%)"></div>
    <div class="flavour-name">STRAWBERRY</div>
    <table class="dates"><tr><td>Expiry Date</td><td>:</td><td>MM/DD/YYYY</td></tr><tr><td>Pkt Date</td><td>:</td><td>MM/DD/YYYY</td></tr><tr><td>MRP</td><td>:</td><td></td></tr></table>
    <div class="maker"><b>Manufacturer</b><br>Manufacturer Name]<br>Address]<br>Contact Number]<br>Email</div>
  </div>

  <div class="label label--toffee">
    <svg class="wave" viewBox="0 0 516 271"><use href="#label-wave" fill="#fff"/></svg>
    <div class="info">
      <b>Ingredients:</b><br>Milk, Strawberries (15%), Sugar,<br>Natural Flavors, Pectin, Live Cultures.
      <div class="nutrition"><div class="nutrition-head">Nutritional Info. (per 100g)</div>
        <table><tr><td>Calories</td><td>120</td></tr><tr><td>Total Fat</td><td>4g</td></tr><tr><td>Saturated Fat</td><td>2.5g</td></tr><tr><td>Carbohydrates</td><td>16g</td></tr><tr><td>Sugars</td><td>14g</td></tr><tr><td>Protein</td><td>5g</td></tr><tr><td>Calcium</td><td>150mg</td></tr></table></div>
      <div class="allergen"><b>Allergen Information:</b> Contains milk.</div>
      <div class="storage"><b>Storage Instructions:</b><br>Keep refrigerated at 4°C or below.<br>Consume within 5 days of opening.</div>
    </div>
    <div class="brand">Nuvelka</div>
    <div class="title">Yogurt</div>
    <div class="flavour-art" role="img" aria-label="Photo of toffee cubes splashing into caramel" style="background:radial-gradient(circle,#e07a2a 30%,#f3a35a 65%,transparent 72%)"></div>
    <div class="flavour-name">TOFFEE</div>
    <table class="dates"><tr><td>Expiry Date</td><td>:</td><td>MM/DD/YYYY</td></tr><tr><td>Pkt Date</td><td>:</td><td>MM/DD/YYYY</td></tr><tr><td>MRP</td><td>:</td><td></td></tr></table>
    <div class="maker"><b>Manufacturer</b><br>Manufacturer Name]<br>Address]<br>Contact Number]<br>Email</div>
  </div>

  <div class="label label--natural">
    <svg class="wave" viewBox="0 0 516 271"><use href="#label-wave" fill="#fff"/></svg>
    <div class="info">
      <b>Ingredients:</b><br>Milk, Strawberries (15%), Sugar,<br>Natural Flavors, Pectin, Live Cultures.
      <div class="nutrition"><div class="nutrition-head">Nutritional Info. (per 100g)</div>
        <table><tr><td>Calories</td><td>120</td></tr><tr><td>Total Fat</td><td>4g</td></tr><tr><td>Saturated Fat</td><td>2.5g</td></tr><tr><td>Carbohydrates</td><td>16g</td></tr><tr><td>Sugars</td><td>14g</td></tr><tr><td>Protein</td><td>5g</td></tr><tr><td>Calcium</td><td>150mg</td></tr></table></div>
      <div class="allergen"><b>Allergen Information:</b> Contains milk.</div>
      <div class="storage"><b>Storage Instructions:</b><br>Keep refrigerated at 4°C or below.<br>Consume within 5 days of opening.</div>
    </div>
    <div class="brand">Nuvelka</div>
    <div class="title">Yogurt</div>
    <div class="flavour-art" role="img" aria-label="Photo of a bowl of creamy natural yogurt" style="background:radial-gradient(circle,#f6f0d8 35%,#cdb98a 68%,transparent 72%)"></div>
    <div class="flavour-name">NATURAL</div>
    <table class="dates"><tr><td>Expiry Date</td><td>:</td><td>MM/DD/YYYY</td></tr><tr><td>Pkt Date</td><td>:</td><td>MM/DD/YYYY</td></tr><tr><td>MRP</td><td>:</td><td></td></tr></table>
    <div class="maker"><b>Manufacturer</b><br>Manufacturer Name]<br>Address]<br>Contact Number]<br>Email</div>
  </div>

  <div class="label label--mango">
    <svg class="wave" viewBox="0 0 516 271"><use href="#label-wave" fill="#fff"/></svg>
    <div class="info">
      <b>Ingredients:</b><br>Milk, Strawberries (15%), Sugar,<br>Natural Flavors, Pectin, Live Cultures.
      <div class="nutrition"><div class="nutrition-head">Nutritional Info. (per 100g)</div>
        <table><tr><td>Calories</td><td>120</td></tr><tr><td>Total Fat</td><td>4g</td></tr><tr><td>Saturated Fat</td><td>2.5g</td></tr><tr><td>Carbohydrates</td><td>16g</td></tr><tr><td>Sugars</td><td>14g</td></tr><tr><td>Protein</td><td>5g</td></tr><tr><td>Calcium</td><td>150mg</td></tr></table></div>
      <div class="allergen"><b>Allergen Information:</b> Contains milk.</div>
      <div class="storage"><b>Storage Instructions:</b><br>Keep refrigerated at 4°C or below.<br>Consume within 5 days of opening.</div>
    </div>
    <div class="brand">Nuvelka</div>
    <div class="title">Yogurt</div>
    <div class="flavour-art" role="img" aria-label="Photo of a cubed mango" style="background:radial-gradient(circle,#f6b21c 40%,#e09010 68%,transparent 72%)"></div>
    <div class="flavour-name">MANGO</div>
    <table class="dates"><tr><td>Expiry Date</td><td>:</td><td>MM/DD/YYYY</td></tr><tr><td>Pkt Date</td><td>:</td><td>MM/DD/YYYY</td></tr><tr><td>MRP</td><td>:</td><td></td></tr></table>
    <div class="maker"><b>Manufacturer</b><br>Manufacturer Name]<br>Address]<br>Contact Number]<br>Email</div>
  </div>

  <div class="theme">Theme 01</div>
</div>
</body>
</html>
```